Sleek, Professional Business Card Design Needed

Business Cards - Logo Attached.

We are a solar consulting company. We are national and want our cards to represent the professional high quality products that we offer.

Industry/Entity Type

Business

Contact Information for Business Card

n/a

Requirements
Must have
• Design
• Name
• Position
• Number
• Email
• Address
Should not have
• Not be too crowded

```html
<!DOCTYPE html>
<html lang="en">
<head>
<meta charset="UTF-8">
<title>Brightfield Solar – Business Card</title>
<link rel="stylesheet" href="https://fonts.googleapis.com/css2?family=Open+Sans:wght@400;600&display=swap">
<style>
  :root {
    --page-bg: #e9ebee;
    --card-bg: #f7f8f9;
    --card-edge: #c9cdd2;
    --brand-blue: #1f73b7;
    --brand-green: #6aa83a;
    --band-blue: #1f73b7;
    --band-text: #e3eaf1;
    --band-name: #dfe6ec;
  }
  * { box-sizing: border-box; margin: 0; padding: 0; }
  html, body {
    width: 1200px;
    height: 970px;
    overflow: hidden;
    background: var(--page-bg);
    font-family: "Open Sans", Arial, sans-serif;
  }
  .canvas {
    position: relative;
    width: 1200px;
    height: 970px;
  }
  .card {
    position: absolute;
    left: 100px;
    top: 207px;
    width: 1000px;
    height: 556px;
    background: var(--card-bg);
    border: 1px solid var(--card-edge);
    border-radius: 26px;
    overflow: hidden;
    box-shadow: 0 10px 30px rgba(0,0,0,0.12);
  }
  .brand {
    position: absolute;
    left: 48px;
    top: 46px;
    width: 330px;
    text-align: center;
  }
  .brand-dot {
    display: block;
    width: 150px;
    height: 150px;
    margin: 0 auto 18px;
    border-radius: 50%;
    background: var(--brand-green);
  }
  .brand-name {
    font-weight: 600;
    font-size: 40px;
    letter-spacing: 0.5px;
    color: var(--brand-blue);
    white-space: nowrap;
  }
  .contact-band {
    position: absolute;
    left: 0;
    top: 323px;
    width: 850px;
    height: 207px;
    background: var(--band-blue);
  }
  .contact {
    position: absolute;
    left: 48px;
    top: 18px;
    color: var(--band-text);
  }
  .person-name {
    font-weight: 600;
    font-size: 27px;
    letter-spacing: 0.5px;
    color: var(--band-name);
    line-height: 1.2;
  }
  .person-role {
    font-size: 22px;
    line-height: 1.2;
    margin-bottom: 18px;
  }
  .contact-line {
    display: flex;
    align-items: center;
    gap: 10px;
    font-size: 23px;
    line-height: 32px;
  }
  .contact-line svg { width: 18px; height: 18px; fill: var(--band-text); }
  .corner-mark {
    position: absolute;
    left: 746px;
    top: 322px;
    width: 212px;
    height: 212px;
    border-radius: 50%;
    background: #ffffff;
  }
</style>
</head>
<body>
<main class="canvas">
  <section class="card">
    <div class="brand">
      <span class="brand-dot"></span>
      <div class="brand-name">BRIGHTFIELD SOLAR</div>
    </div>

    <div class="contact-band">
      <div class="contact">
        <div class="person-name">DANIEL MARSH</div>
        <div class="person-role">Managing Director</div>
        <div class="contact-line">
          <svg viewBox="0 0 24 24" aria-hidden="true"><path d="M3 9c0-3 4-5 9-5s9 2 9 5v2h-5V9c-1-1-7-1-8 0v2H3z M6 12h12l2 8H4z"/></svg>
          <span>+ 000 000 0000</span>
        </div>
        <div class="contact-line">
          <svg viewBox="0 0 24 24" aria-hidden="true"><path d="M2 5h20v14H2z M3.5 6.5 12 13l8.5-6.5" stroke="#1f73b7" stroke-width="1.5"/></svg>
          <span>daniel@brightfieldsolar.com</span>
        </div>
        <div class="contact-line">
          <span>118 west 52nd street, New York, NY 10019</span>
        </div>
      </div>
    </div>

    <div class="corner-mark" aria-hidden="true"></div>
  </section>
</main>
</body>
</html>
```